Helicopter scenic /Charter company

Need a sign 920mm x 920mm for our Marlow Helipad fence that catches the eye for people walking past. Some photos have been attached but feel free to use helicopter photos you have as well. Like the sign to be black with lettering that stands out. You may do a design with photos or it may look better without. It is up to you. It just has to look eye catching and exciting.
Text: Helicopter Joy Flights & Scenic Tours here seven days from October to March. Prices from just $99 per person* Details at wendaloft.com.au or ph 9372 6105
* $99 flights are shared 8 minute flights and are only available on weekends

Target Market(s)

Tourists locals walking past the helipad

Requirements
Must have
• Logo
• Text as in project description

```html
<!DOCTYPE html>
<html lang="en">
<head>
<meta charset="utf-8">
<title>Wendaloft Helicopters – Joy Flights Sign</title>
<link rel="stylesheet" href="https://fonts.googleapis.com/css2?family=Black+Ops+One&family=PT+Sans:wght@400;700&family=Arimo&display=swap">
<style>
  :root{
    --yellow:#ffd704;
    --gold:#d39e12;
    --amber:#fdb913;
    --navy:#1c3f7c;
    --headline-blue:#1f68c9;
    --headline-shadow:#0b2550;
    --deep-blue:#1d4fa3;
    --ink:#0c0c0c;
    --white:#ffffff;
    --logo-grey:#cfd8e8;
    --sky-light:#b9def5;
    --sky-mid:#52aee6;
    --sky-deep:#1a8ad6;
  }
  html,body{margin:0;padding:0;overflow:hidden;background:var(--white);}
  .sign{display:block;width:1200px;height:1200px;}
  .headline{font-family:"Black Ops One",system-ui,sans-serif;font-size:72px;}
  .headline-face{fill:var(--headline-blue);}
  .headline-shade{fill:var(--headline-shadow);}
  .body-text{font-family:"PT Sans",sans-serif;}
  .season-number{font-size:100px;fill:var(--deep-blue);}
  .season-key{font-size:48px;font-weight:700;fill:var(--deep-blue);}
  .season-plain{font-size:48px;fill:var(--ink);}
  .price-label{font-size:44px;font-weight:700;fill:var(--ink);}
  .price-sub{font-size:38px;fill:var(--ink);}
  .price-amount{font-size:160px;font-weight:700;fill:var(--ink);letter-spacing:-4px;}
  .price-note{font-size:29px;fill:var(--ink);}
  .brand-name{font-size:44px;font-weight:700;fill:var(--logo-grey);}
  .web-address{font-size:38px;fill:var(--white);}
  .web-domain{fill:var(--yellow);}
  .phone-number{font-size:82px;font-weight:700;fill:var(--yellow);}
  .footnote{font-family:"Arimo",Arial,sans-serif;font-size:25px;fill:var(--yellow);}
</style>
</head>
<body>
<svg class="sign" viewBox="185 185 1132 1132" xmlns="http://www.w3.org/2000/svg">
  <defs>
    <linearGradient id="skyTone" x1="0" y1="1" x2="1" y2="0">
      <stop offset="0" stop-color="var(--sky-light)"/>
      <stop offset="0.5" stop-color="var(--sky-mid)"/>
      <stop offset="1" stop-color="var(--sky-deep)"/>
    </linearGradient>
  </defs>

  <g class="sky-photo" role="img" aria-label="Photo of a white and blue helicopter flying through a bright blue sky with soft clouds">
    <rect x="185" y="185" width="1132" height="1132" fill="url(#skyTone)"/>
  </g>

  <polygon class="band-navy" points="905,470 1317,400 1317,553" fill="var(--navy)"/>
  <polygon class="band-gold" points="185,585 1317,355 1317,400 905,470" fill="var(--gold)"/>
  <polygon class="band-yellow" points="185,185 1317,185 1317,355 185,585" fill="var(--yellow)"/>

  <g class="headline">
    <g transform="matrix(1 0 -0.176 1 55.7 0)">
      <text class="headline-shade" x="268" y="320" textLength="950" lengthAdjust="spacingAndGlyphs">HELICOPTER JOY FLIGHTS</text>
      <text class="headline-face" x="264" y="316" textLength="950" lengthAdjust="spacingAndGlyphs">HELICOPTER JOY FLIGHTS</text>
    </g>
    <g transform="matrix(1 0 -0.176 1 71.8 0)">
      <text class="headline-shade" x="268" y="412" textLength="612" lengthAdjust="spacingAndGlyphs">&amp; SCENIC TOURS</text>
      <text class="headline-face" x="264" y="408" textLength="612" lengthAdjust="spacingAndGlyphs">&amp; SCENIC TOURS</text>
    </g>
  </g>

  <polygon class="season-banner" points="338,588 1163,588 1198,623 1198,677 1163,712 338,712 303,677 303,623" fill="var(--amber)"/>
  <polygon points="342,598 1159,598 1188,627 1188,673 1159,702 342,702 313,673 313,627" fill="none" stroke="var(--white)" stroke-width="2"/>
  <g class="body-text">
    <text class="season-number" x="400" y="688">7</text>
    <text class="season-key" x="466" y="672" textLength="102" lengthAdjust="spacingAndGlyphs">Days</text>
    <text class="season-plain" x="582" y="672" textLength="103" lengthAdjust="spacingAndGlyphs">from</text>
    <text class="season-key" x="698" y="672" textLength="177" lengthAdjust="spacingAndGlyphs">October</text>
    <text class="season-plain" x="889" y="672" textLength="44" lengthAdjust="spacingAndGlyphs">to</text>
    <text class="season-key" x="947" y="672" textLength="150" lengthAdjust="spacingAndGlyphs">March.</text>
  </g>

  <polygon class="price-badge" points="205,925 290,757 507,757 592,925 507,1092 290,1092" fill="var(--amber)"/>
  <polygon points="218,925 297,768 500,768 579,925 500,1081 297,1081" fill="none" stroke="var(--white)" stroke-width="2"/>
  <g class="body-text" text-anchor="middle">
    <text class="price-label" x="399" y="818">Prices</text>
    <text class="price-sub" x="399" y="862">from just</text>
    <text class="price-amount" x="399" y="1005">$99</text>
    <text class="price-note" x="399" y="1062">per person*</text>
  </g>

  <polygon class="band-footer" points="185,1157 1317,1050 1317,1317 185,1317" fill="var(--navy)"/>

  <circle cx="282" cy="1207" r="30" fill="var(--yellow)"/>
  <text class="body-text brand-name" x="330" y="1202" textLength="333" lengthAdjust="spacingAndGlyphs">WENDALOFT</text>
  <text class="body-text brand-name" x="358" y="1244" textLength="305" lengthAdjust="spacingAndGlyphs">HELICOPTERS</text>

  <text class="body-text web-address" x="787" y="1152" textLength="446" lengthAdjust="spacingAndGlyphs">www.<tspan class="web-domain">wendaloft</tspan>.com.au</text>
  <g class="phone-icon" fill="none" stroke="var(--white)" stroke-width="4">
    <circle cx="823" cy="1210" r="32"/>
    <path d="M808,1194 q-6,6 0,18 q8,16 22,22 q10,4 16,-2 l-8,-9 q-4,4 -9,0 q-8,-6 -12,-14 q-2,-5 2,-8 z" fill="var(--white)" stroke-width="1.5"/>
    <path d="M826,1190 a20,20 0 0 1 18,18" stroke-width="3"/>
    <path d="M826,1198 a12,12 0 0 1 10,10" stroke-width="3"/>
  </g>
  <text class="body-text phone-number" x="888" y="1240" textLength="345" lengthAdjust="spacingAndGlyphs">9372 6105</text>

  <text class="footnote" x="287" y="1295" textLength="928" lengthAdjust="spacingAndGlyphs">* $99 flights are shared 8 minute flights and are only available on weekends</text>
</svg>
</body>
</html>
```